Business Card - connecting 2 souls and beggining the journey of self discovery

Logo on the front
with tag line

On the back list of services and contact details

Seminars
workshops
Coaching
podcasts

Darren Whitlow
Health & Wellbeing Life Coach
0468 215 937
darren@wearebrightroots.net
wearebrightroots.net

Industry/Entity Type

Life Coaching

Contact Information for Business Card

I like the use of colour from the logo to be used. I'm not a fan of white.

Requirements
Must have
• My tagline: Your path inward begins today
Nice to have
• Use of colour that is in the mind body soul logo

```html
<!DOCTYPE html>
<html lang="en">
<head>
<meta charset="utf-8">
<title>Bright Roots Wellness – Business Card</title>
<link href="https://fonts.googleapis.com/css2?family=Montserrat:wght@500;600&family=Open+Sans:wght@400;700&display=swap" rel="stylesheet">
<style>
  :root {
    --bg: #3a3a3c;
    --card: #ffffff;
    --grey: #6d6e71;
    --ink: #3b3b3d;
    --orange: #f28c28;
    --coral: #ee5a5f;
    --pink: #ee6670;
    --amber: #f5913f;
    --green: #64bd8a;
    --shadow: rgba(0,0,0,0.35);
  }
  * { box-sizing: border-box; margin: 0; padding: 0; }
  html, body { width: 1200px; height: 1000px; overflow: hidden; }
  body {
    background: var(--bg);
    font-family: "Open Sans", Arial, sans-serif;
    position: relative;
  }
  .card {
    position: absolute;
    width: 560px;
    height: 320px;
    background: var(--card);
    border-radius: 18px;
    overflow: hidden;
    box-shadow: 0 12px 30px var(--shadow);
  }
  /* Front */
  .card--front { left: 320px; top: 100px; }
  .front__brand {
    position: absolute; left: 0; right: 0; top: 92px;
    display: flex; flex-direction: column; align-items: center;
  }
  .front__dot {
    width: 62px; height: 62px; border-radius: 50%;
    background: var(--orange);
    margin-bottom: 14px;
  }
  .front__name {
    font-family: "Montserrat", Arial, sans-serif;
    font-weight: 600; font-size: 26px; letter-spacing: -1px;
    color: var(--grey);
  }
  .front__tagline {
    margin-top: 34px;
    font-size: 11px; letter-spacing: 4px; text-transform: uppercase;
    color: var(--ink);
  }
  /* Back */
  .card--back { left: 320px; top: 560px; }
  .back__band {
    position: absolute; inset: 0;
    background: linear-gradient(180deg, var(--pink) 0%, var(--amber) 50%, var(--green) 100%);
    clip-path: polygon(74% 0, 100% 0, 100% 100%, 60% 100%);
  }
  .back__disc {
    position: absolute; left: 318px; top: 110px;
    width: 170px; height: 170px; border-radius: 50%;
    background: var(--card);
    box-shadow: 0 0 0 4px rgba(255,255,255,0.55);
  }
  .back__content { position: absolute; left: 30px; top: 26px; }
  .back__brand {
    font-family: "Montserrat", Arial, sans-serif;
    font-weight: 600; font-size: 24px; letter-spacing: -1px;
    color: var(--grey);
  }
  .back__person { margin-top: 14px; }
  .back__name {
    font-weight: 700; font-size: 20px; text-transform: uppercase; line-height: 1.1;
  }
  .back__name .first { color: var(--orange); }
  .back__name .last { color: var(--coral); }
  .back__role { font-size: 15px; color: var(--grey); }
  .back__contacts { margin-top: 16px; list-style: none; }
  .back__contacts li {
    display: flex; align-items: center; gap: 8px;
    font-size: 13px; color: var(--ink); line-height: 1.45;
  }
  .back__contacts svg { width: 11px; height: 11px; flex: none; }
  .back__contacts .accent { color: var(--coral); }
  .back__services {
    position: absolute; left: 30px; bottom: 26px;
    font-size: 13.5px; color: var(--ink); letter-spacing: 0.2px;
  }
</style>
</head>
<body>

<section class="card card--front">
  <div class="front__brand">
    <span class="front__dot"></span>
    <span class="front__name">Bright Roots Wellness</span>
    <span class="front__tagline">Your path inward begins today</span>
  </div>
</section>

<section class="card card--back">
  <div class="back__band"></div>
  <div class="back__disc"></div>
  <div class="back__content">
    <div class="back__brand">Bright Roots Wellness</div>
    <div class="back__person">
      <div class="back__name"><span class="first">Darren</span> <span class="last">Whitlow</span></div>
      <div class="back__role">Life Coach</div>
    </div>
    <ul class="back__contacts">
      <li>
        <svg viewBox="0 0 12 12"><rect x="3" y="0.5" width="6" height="11" rx="1.2" fill="none" stroke="#ee5a5f" stroke-width="1.2"/><circle cx="6" cy="9.5" r="0.7" fill="#ee5a5f"/></svg>
        0468 215 937
      </li>
      <li>
        <svg viewBox="0 0 12 12"><rect x="0.5" y="2" width="11" height="8" fill="#ee5a5f"/><path d="M0.5 2 L6 7 L11.5 2" fill="none" stroke="#fff" stroke-width="1"/></svg>
        darren@wearebrightroots.net
      </li>
      <li>
        <svg viewBox="0 0 12 12"><circle cx="6" cy="6" r="5.3" fill="#ee5a5f"/><path d="M0.7 6 H11.3 M6 0.7 V11.3 M6 0.7 C3 3.5 3 8.5 6 11.3 M6 0.7 C9 3.5 9 8.5 6 11.3" fill="none" stroke="#fff" stroke-width="0.7"/></svg>
        <span>www.<span class="accent">wearebrightroots</span>.net</span>
      </li>
    </ul>
  </div>
  <div class="back__services">Seminars | Workshops | Coaching | Podcasts</div>
</section>

</body>
</html>
```